Regional Showdown Flyer for Holiday Program

Need a one page flyer, can be back to front or one page, ensuring you can fit all information, colourful, aimed at a market of 8-13 year old boys and girls.
The flyer needs to be noticed, needs to have certain information on it and needs to be Autralian Rule Football orientated.
Have uploaded file so you can understand the style (not content), style of flyer I am looking at getting submitted.

Target Market(s)

8-13 year old boys and girls and their parents.

Requirements
Must have
• Regional Showdown Event
• Price for Regional Showdown Day will be $85
• Strictly Limited Places, only the best footballers should enter this challenge
• Inaugural event, be the first Regional Showdown Winner for your age!
• Do you love a challenge! Put yourself to the test!
• Are you up to it - Water Slide Goal Kicking Contest! The fastest kick in the West (tested by our very own speed gun)! Can you survive the Footy Titan Trail or Last One Standing Goal Kicking! These challenges are crazy are super fun!
• If you think you can deliver on the big stage then this is for YOU!
• All District age winners will receive prizes, awards and the adulation from all their peers!
• Year's 3-5 from 9am to 12pm
• Year's 6-8 from 1-4pm
• All challengers compete against their own age
• Lunch Provided
• Monday 16th April - Upper Tarrowby Regional Showdown Day at Tarrowby Oval
• Tuesday 17th April - North Tarrowby Regional Showdown Day at Kilmorna Reserve
• Wednesday 18th April - Yarlo Regional Showdown Day - Dunhaven Football Club
• Every Challenge Participant receives a District Football!
• Need to put all 3 District Football Logos on the bottom of the flyer, logos attached at bottom.
Nice to have
• Plenty of colour, if you can fit all information on one page that would be fine
Should not have
• Dull, boring, any footballs should be Aussie Rules footballs not NFL or soccer

```html
<!DOCTYPE html>
<html lang="en">
<head>
<meta charset="utf-8">
<title>Regional Showdown Flyer</title>
<link href="https://fonts.googleapis.com/css2?family=Luckiest+Guy&family=Nunito:wght@700;800;900&display=swap" rel="stylesheet">
<style>
  :root {
    --stage: #d3d3d3;
    --navy: #14306b;
    --navy-deep: #0d2152;
    --red: #d81e2a;
    --blue: #1f4fc4;
    --yellow: #ffe11a;
    --green: #19a34a;
    --white: #ffffff;
    --magenta: #e3247f;
    --pink: #f05aa8;
    --cyan: #5fd2f0;
    --orange: #ff9a2e;
    --display: "Luckiest Guy", "Nunito", sans-serif;
  }
  * { box-sizing: border-box; margin: 0; padding: 0; }
  html, body { width: 1200px; height: 800px; overflow: hidden; }
  body { background: var(--stage); font-family: "Nunito", sans-serif; }

  .flyer {
    position: absolute; left: 330px; top: 20px;
    width: 540px; height: 760px; overflow: hidden;
    box-shadow: 0 6px 18px rgba(0,0,0,.25);
  }
  .flyer__backdrop {
    position: absolute; inset: 0;
    background:
      radial-gradient(circle at 50% 30%, #ffffff 0, #e9f3ff 18%, transparent 42%),
      radial-gradient(circle at 10% 60%, var(--orange) 0, transparent 30%),
      radial-gradient(circle at 90% 10%, var(--cyan) 0, transparent 30%),
      radial-gradient(circle at 85% 85%, var(--pink) 0, transparent 35%),
      linear-gradient(160deg, var(--magenta), #b5198f 50%, var(--magenta));
  }

  .title {
    position: absolute; left: 30px; top: 22px;
    font-family: var(--display); font-weight: 900;
    transform: rotate(-4deg); transform-origin: left top;
    line-height: .95; text-transform: uppercase;
  }
  .title__line {
    display: block; font-size: 60px; color: var(--white);
    -webkit-text-stroke: 3px var(--navy-deep);
    paint-order: stroke fill;
    text-shadow: 4px 4px 0 var(--navy-deep);
    letter-spacing: 1px;
  }
  .title__event {
    display: block; margin: 8px 0 0 90px; font-size: 66px;
    color: var(--red); -webkit-text-stroke: 3px var(--white);
    paint-order: stroke fill;
    text-shadow: 3px 3px 0 var(--navy-deep);
  }
  .title__event span { color: var(--blue); }

  .intro {
    position: absolute; left: 26px; top: 246px; width: 470px;
    font-family: var(--display); font-weight: 900; font-size: 16px; line-height: 1.15;
    color: var(--navy-deep); transform: rotate(-3deg); text-transform: uppercase;
  }
  .intro__call { color: var(--green); display: block; margin-top: 4px; }
  .intro__call em { font-style: normal; color: var(--red); }

  .ribbon {
    position: absolute; right: 12px; width: 300px;
    font-family: var(--display); font-weight: 900; color: var(--white);
    padding: 7px 14px; line-height: 1.1; transform: rotate(-4deg);
    text-transform: uppercase;
  }
  .ribbon--price { top: 318px; height: 50px; background: var(--navy); font-size: 14px; display: flex; align-items: center; justify-content: space-between; gap: 8px; }
  .ribbon--price .ribbon__amount { font-size: 30px; color: var(--yellow); }
  .ribbon--limit { top: 374px; height: 44px; background: var(--red); font-size: 12px; text-align: center; display: flex; align-items: center; justify-content: center; }

  .ball {
    position: absolute; left: 18px; top: 424px; width: 250px; height: 148px;
    background: radial-gradient(ellipse at 40% 35%, #ff5a4e, #d3140f 60%, #9d0b08);
    border-radius: 50%;
  }

  .details {
    position: absolute; right: 14px; top: 428px; width: 240px;
    background: var(--navy); color: var(--white);
    padding: 10px 12px 10px 36px; font-size: 9.5px; line-height: 1.3; font-weight: 800;
  }
  .details p { margin-bottom: 6px; position: relative; }
  .details p:last-child { margin-bottom: 0; }
  .details .tick {
    position: absolute; left: -28px; top: 0; width: 20px; height: 20px;
  }
  .details__times { font-family: var(--display); font-size: 12px; font-weight: 900; line-height: 1.25; }
  .details__note { font-size: 8px; display: block; font-family: "Nunito", sans-serif; font-weight: 700; }
  .details__lunch { font-family: var(--display); font-size: 12px; font-weight: 900; }

  .dates {
    position: absolute; left: 18px; top: 584px; width: 258px;
    background: var(--navy); color: var(--white);
    padding: 8px 10px 8px 12px; list-style: none;
    font-size: 9px; line-height: 1.25; font-weight: 800;
  }
  .dates li { position: relative; padding-left: 14px; margin-bottom: 3px; }
  .dates li:last-child { margin-bottom: 0; }
  .dates li::before {
    content: ""; position: absolute; left: 0; top: 3px;
    width: 7px; height: 7px; border-radius: 50%; background: var(--yellow);
  }

  .partners {
    position: absolute; left: 18px; top: 708px; width: 504px; height: 42px;
    background: var(--white); border-radius: 10px;
    display: flex; align-items: center; justify-content: space-around; padding: 0 10px;
  }
  .partner {
    display: flex; align-items: center; gap: 6px;
    font-family: var(--display); font-weight: 900; font-size: 12px; color: var(--navy);
    text-transform: uppercase;
  }
  .partner__dot { width: 14px; height: 14px; border-radius: 50%; background: var(--navy); }
</style>
</head>
<body>
  <main class="flyer">
    <div class="flyer__backdrop" role="img" aria-label="Colourful paint splash background in magenta, pink, orange and cyan"></div>

    <h1 class="title">
      <span class="title__line">Regional</span>
      <span class="title__line">Showdown</span>
      <span class="title__event"><span>E</span>vent</span>
    </h1>

    <p class="intro">
      Inaugural event. Be the first Regional Showdown winner for your age!
      <span class="intro__call">Do you love a <em>challenge!</em> Put yourself to the test!</span>
    </p>

    <div class="ribbon ribbon--price">
      <span>Price for Regional Showdown Day will be</span>
      <span class="ribbon__amount">$85</span>
    </div>
    <div class="ribbon ribbon--limit">Strictly limited places, only the best footballers should enter this challenge</div>

    <div class="ball" role="img" aria-label="Red Aussie Rules football"></div>

    <section class="details">
      <p>
        <svg class="tick" viewBox="0 0 24 24" aria-hidden="true"><circle cx="12" cy="12" r="11" fill="#ffe11a"/><path d="M6 12.5l4 4 8-9" fill="none" stroke="#14306b" stroke-width="3" stroke-linecap="round" stroke-linejoin="round"/></svg>
        Are you up to it - Water Slide Goal Kicking Contest! The fastest kick in the West (tested by our very own speed gun)! Can you survive the Footy Titan Trail or Last One Standing Goal Kicking! These challenges are crazy are super fun!
      </p>
      <p>
        <svg class="tick" viewBox="0 0 24 24" aria-hidden="true"><circle cx="12" cy="12" r="11" fill="#ffe11a"/><path d="M6 12.5l4 4 8-9" fill="none" stroke="#14306b" stroke-width="3" stroke-linecap="round" stroke-linejoin="round"/></svg>
        If you think you can deliver on the big stage then this is for YOU!
      </p>
      <p>
        <svg class="tick" viewBox="0 0 24 24" aria-hidden="true"><circle cx="12" cy="12" r="11" fill="#ffe11a"/><path d="M6 12.5l4 4 8-9" fill="none" stroke="#14306b" stroke-width="3" stroke-linecap="round" stroke-linejoin="round"/></svg>
        All District age winners will receive prizes, awards and the adulation from all their peers!
      </p>
      <p class="details__times">
        <svg class="tick" viewBox="0 0 24 24" aria-hidden="true"><circle cx="12" cy="12" r="11" fill="#ffe11a"/><path d="M6 12.5l4 4 8-9" fill="none" stroke="#14306b" stroke-width="3" stroke-linecap="round" stroke-linejoin="round"/></svg>
        Year's 3-5 from 9am to 12pm<br>Year's 6-8 from 1-4pm
        <span class="details__note">All challengers compete against their own age</span>
      </p>
      <p class="details__lunch">
        <svg class="tick" viewBox="0 0 24 24" aria-hidden="true"><circle cx="12" cy="12" r="11" fill="#ffe11a"/><path d="M6 12.5l4 4 8-9" fill="none" stroke="#14306b" stroke-width="3" stroke-linecap="round" stroke-linejoin="round"/></svg>
        Lunch Provided
      </p>
    </section>

    <ul class="dates">
      <li>Monday 16th April - Upper Tarrowby Regional Showdown Day at Tarrowby Oval</li>
      <li>Tuesday 17th April - North Tarrowby Regional Showdown Day at Kilmorna Reserve</li>
      <li>Wednesday 18th April - Yarlo Regional Showdown Day - Dunhaven Football Club</li>
      <li>Every Challenge Participant receives a District Football!</li>
    </ul>

    <footer class="partners">
      <span class="partner"><span class="partner__dot"></span>Coastal District</span>
      <span class="partner"><span class="partner__dot"></span>Ridgeback District</span>
      <span class="partner"><span class="partner__dot"></span>Yarlo District</span>
    </footer>
  </main>
</body>
</html>
```